PELDRAX Business Cards

We require a business card for our company that provides IT consulting services. We already have a logo that needs to be used on the card. We want a clean professional looking design that incorporates our colours. Our main focus is providing managed services to business, which involves us looking after all of their IT requirements including managing servers/networks, projects, and procurement.

Industry/Entity Type

Information Technology

Requirements
Must have
• our logo, contact information, name, title, phone numbers

```html
<!DOCTYPE html>
<html lang="en">
<head>
<meta charset="utf-8">
<title>PELDRAX Business Card</title>
<link href="https://fonts.googleapis.com/css2?family=Noto+Sans:wght@400;500;600&display=swap" rel="stylesheet">
<style>
  :root {
    --page-bg: #e6e3de;
    --card-bg: #f2f3f4;
    --brand-blue: #2a7ab0;
    --brand-blue-deep: #155d92;
    --swoosh-dark: #1c1d20;
    --text-dark: #2b2d30;
    --text-mid: #3a3c40;
    --map-tone: #d9dcdf;
  }
  html, body {
    margin: 0;
    padding: 0;
    width: 1200px;
    height: 970px;
    overflow: hidden;
    background: var(--page-bg);
  }
  .business-card {
    position: absolute;
    left: 67px;
    top: 190px;
    width: 1066px;
    height: 590px;
    border-radius: 26px;
    background: var(--card-bg);
    box-shadow: 0 0 0 2px #d6dadd, 0 14px 40px rgba(0,0,0,0.12);
    overflow: hidden;
    font-family: "Noto Sans", sans-serif;
    color: var(--text-dark);
  }
  .card-art {
    position: absolute;
    inset: 0;
  }
  .world-map-area {
    position: absolute;
    left: 300px;
    top: 110px;
    width: 660px;
    height: 310px;
    border-radius: 50%;
    background: radial-gradient(ellipse at center, var(--map-tone) 0%, rgba(217,220,223,0.5) 55%, rgba(217,220,223,0) 75%);
  }
  .brand {
    position: absolute;
    left: 72px;
    top: 52px;
    display: flex;
    align-items: center;
    gap: 18px;
  }
  .brand-dot {
    width: 62px;
    height: 62px;
    border-radius: 50%;
    background: var(--brand-blue);
  }
  .brand-name {
    font-size: 72px;
    font-weight: 600;
    letter-spacing: 4px;
    color: var(--brand-blue);
    line-height: 1;
  }
  .person-name {
    position: absolute;
    left: 70px;
    top: 176px;
    margin: 0;
    font-size: 34px;
    font-weight: 500;
    color: var(--text-dark);
  }
  .person-title {
    position: absolute;
    left: 73px;
    top: 218px;
    margin: 0;
    font-size: 26px;
    font-weight: 400;
    color: var(--text-mid);
  }
  .contact-list {
    position: absolute;
    left: 70px;
    top: 281px;
    margin: 0;
    padding: 0;
    list-style: none;
  }
  .contact-item {
    display: flex;
    align-items: center;
    height: 35px;
    font-size: 25px;
    color: var(--text-mid);
  }
  .contact-icon {
    width: 32px;
    height: 26px;
    margin-right: 8px;
    flex: none;
  }
  .contact-icon * { fill: none; stroke: #4b4e53; stroke-width: 2; }
  .contact-icon .solid { fill: #4b4e53; stroke: none; }
</style>
</head>
<body>
  <div class="business-card">
    <div class="world-map-area" role="img" aria-label="Faint world map in the background"></div>

    <svg class="card-art" viewBox="0 0 1066 590" width="1066" height="590" aria-hidden="true">
      <defs>
        <linearGradient id="band-blue" x1="0" y1="0" x2="1" y2="1">
          <stop offset="0" stop-color="#4a93c4"/>
          <stop offset="0.6" stop-color="#2a7ab0"/>
          <stop offset="1" stop-color="#155d92"/>
        </linearGradient>
      </defs>
      <path d="M920,0 H1066 V590 H0 V580 C120,530 260,490 380,488 C520,488 620,530 740,535 C880,540 990,460 993,300 C995,200 970,80 920,0 Z" fill="url(#band-blue)"/>
      <path d="M560,512 C640,525 700,535 760,536 C900,540 990,440 990,210 C1000,420 930,535 760,540 C690,541 630,530 560,512 Z" fill="var(--swoosh-dark)"/>
      <path d="M6,572 C50,545 110,520 170,505 C120,525 60,552 10,580 Z" fill="var(--swoosh-dark)"/>
    </svg>

    <div class="brand">
      <span class="brand-dot"></span>
      <span class="brand-name">PELDRAX</span>
    </div>

    <h1 class="person-name">Mara Hollis</h1>
    <p class="person-title">Manager</p>

    <ul class="contact-list">
      <li class="contact-item">
        <svg class="contact-icon" viewBox="0 0 32 26"><rect x="10" y="2" width="12" height="22" rx="2"/><circle class="solid" cx="16" cy="20" r="1.4"/></svg>
        +01 415 382 627
      </li>
      <li class="contact-item">
        <svg class="contact-icon" viewBox="0 0 32 26"><path d="M7,4 L11,4 L13,9 L10.5,11 C12,14.5 14.5,17 18,18.5 L20,16 L25,18 L25,22 C15,23 6,14 7,4 Z"/><path d="M18,4 A6,6 0 0 1 24,10"/><path d="M18,8 A2.5,2.5 0 0 1 20.5,10.5"/></svg>
        +01 415 382 627
      </li>
      <li class="contact-item">
        <svg class="contact-icon" viewBox="0 0 32 26"><rect x="2" y="4" width="28" height="18"/><path d="M2,4 L16,15 L30,4 M2,22 L12,12 M30,22 L20,12"/></svg>
        info@PELDRAX .com
      </li>
      <li class="contact-item">
        <svg class="contact-icon" viewBox="0 0 32 26"><circle cx="16" cy="13" r="11"/><ellipse cx="16" cy="13" rx="5" ry="11"/><path d="M5,13 H27 M7,7 H25 M7,19 H25"/></svg>
        www.PELDRAX .com
      </li>
      <li class="contact-item">
        <svg class="contact-icon" viewBox="0 0 32 26"><path class="solid" d="M16,2 C11,2 8,5.5 8,10 C8,15 16,24 16,24 C16,24 24,15 24,10 C24,5.5 21,2 16,2 Z M16,7 A3,3 0 1 1 16,13 A3,3 0 1 1 16,7 Z"/></svg>
        2740 Cedar Ridge Lane, Port Halden, Oregon, 97512
      </li>
    </ul>
  </div>
</body>
</html>
```